Bottle label design for a mulberry brandy

Please create a label design for a mulberry brandy. The registered brand name is "Kolvat"
The brandy will be produced in Armenia from 100% mulberry.
Color of the product: transparent.
The product will be sold worldwide. The price will be between 30 and 50 USD. So the product will be in premium category.
Therefore we need a solid design, appropriate to the product price category. The design, however, needs to be modern and optimistic.
You can have mulberries on the label or not have, it is up to you.
We have chosen for the product some bottle types, the links to the available bottles you can find in the attachment. Ideally you show a picture of your label on the bottle you selected.

Target Market(s)

worldwide

```html
<!DOCTYPE html>
<html lang="en">
<head>
<meta charset="utf-8">
<title>Kolvat Mulberry Brandy – Label</title>
<link rel="stylesheet" href="https://fonts.googleapis.com/css2?family=Bodoni+Moda:opsz,wght@6..96,400&family=Inter:wght@300;400&display=swap">
<style>
  :root {
    --paper: #ffffff;
    --capsule-red: #f20000;
    --label-red: #e3000b;
    --gold: #8c6c47;
    --gold-line: #a88a64;
  }
  html, body {
    margin: 0;
    padding: 0;
    overflow: hidden;
    background: var(--paper);
  }
  .canvas {
    position: relative;
    width: 927px;
    height: 1200px;
    background: var(--paper);
    overflow: hidden;
    font-family: "Inter", Helvetica, Arial, sans-serif;
  }

  /* Neck capsule */
  .capsule {
    position: absolute;
    left: 384px;
    top: 35px;
    width: 164px;
    height: 295px;
    background: var(--capsule-red);
    border-radius: 6px 6px 2px 2px;
  }
  .capsule-art {
    position: absolute;
    left: 0;
    top: 0;
    width: 164px;
    height: 295px;
  }
  .capsule-rule {
    fill: var(--gold-line);
  }
  .capsule-name {
    font-family: "Bodoni Moda", "Didot", serif;
    font-weight: 400;
    font-size: 54px;
    fill: var(--paper);
  }

  /* Front label */
  .label-text {
    position: absolute;
    left: 0;
    width: 100%;
    margin: 0;
    text-align: center;
    color: var(--label-red);
  }
  .content-note {
    top: 478px;
    font-size: 14px;
    font-weight: 300;
  }
  .brand-name {
    position: absolute;
    left: 0;
    top: 660px;
    width: 927px;
    height: 80px;
    margin: 0;
  }
  .brand-name text {
    font-family: "Bodoni Moda", "Didot", serif;
    font-weight: 400;
    font-size: 64px;
    fill: var(--gold);
  }
  .brand-rule {
    position: absolute;
    left: 270px;
    width: 399px;
    top: 746px;
    height: 2px;
    background: var(--gold-line);
  }
  .product-type {
    top: 856px;
    font-size: 15px;
    font-weight: 300;
    letter-spacing: 4.5px;
  }
  .origin {
    top: 881px;
    font-size: 9.5px;
    font-weight: 300;
  }
  .volume {
    top: 1020px;
    font-size: 14px;
    font-weight: 300;
  }
</style>
</head>
<body>
  <main class="canvas">
    <div class="capsule">
      <svg class="capsule-art" viewBox="0 0 164 295" aria-label="KOLVAT">
        <rect class="capsule-rule" x="10" y="76" width="144" height="3"/>
        <text class="capsule-name" transform="translate(101,180) rotate(-90)" text-anchor="middle" textLength="175" lengthAdjust="spacingAndGlyphs">KOLVAT</text>
      </svg>
    </div>

    <p class="label-text content-note">100% mulberry</p>
    <h1 class="brand-name">
      <svg width="927" height="80" viewBox="0 0 927 80" aria-label="KOLVAT">
        <text x="466" y="68" text-anchor="middle" textLength="213" lengthAdjust="spacingAndGlyphs">KOLVAT</text>
      </svg>
    </h1>
    <div class="brand-rule"></div>
    <p class="label-text product-type">MULBERRY BRANDY</p>
    <p class="label-text origin">product of Armenia</p>
    <p class="label-text volume">Vol%40 500ml</p>
  </main>
</body>
</html>
```